Massage therapist LMT

I need something simple and beautiful I'm a man no flowers, no leafs,no tree please

Target Market(s)

People who suffer ( body pain,stess,body injury ect.. )

Industry/Entity Type

Massage Therapy

Contact Information for Business Card

Garrick T Valbonne LMT

Font styles to use
Serif
Script

Colors

Designer to choose colors to be used in the design.

Requirements
Must have
• Get a massage
• For the
• Health
• Of it
Nice to have
• Skeleton
Should not have
• No flowers
• No tree

```html
<!DOCTYPE html>
<html lang="en">
<head>
<meta charset="utf-8">
<title>Garrick T Valbonne LMT – Business Card</title>
<link href="https://fonts.googleapis.com/css2?family=Tinos:ital,wght@0,400;0,700;1,400;1,700&family=Pinyon+Script&display=swap" rel="stylesheet">
<style>
  :root {
    --stage: #3a3a3a;
    --card: #121212;
    --ink: #ffffff;
    --ink-soft: #e9cfc3;
    --muscle-light: #d88a6c;
    --muscle-mid: #b8614a;
    --muscle-deep: #7a3426;
  }
  * { margin: 0; padding: 0; box-sizing: border-box; }
  html, body {
    width: 1189px; height: 1200px; overflow: hidden;
    background: var(--stage);
  }
  .sheet { position: relative; width: 1189px; height: 1200px; }
  .card {
    position: absolute; top: 233px; width: 437px; height: 764px;
    background: var(--card); overflow: hidden;
    font-family: "Tinos", "Times New Roman", serif; color: var(--ink);
  }
  .card--front { left: 121px; }
  .card--back { left: 577px; }
  .anatomy { position: absolute; top: 0; height: 100%; }
  .card--front .anatomy { left: 160px; width: 277px; }
  .card--back .anatomy { left: 0; width: 290px; }
  .name-block {
    position: absolute; left: 42px; top: 724px;
    transform: rotate(-90deg); transform-origin: 0 0;
    white-space: nowrap;
  }
  .name-block__name {
    font-weight: 700; font-style: italic; font-size: 80px; line-height: 1;
    letter-spacing: 0.5px;
  }
  .name-block__title {
    position: absolute; right: 0; top: 88px;
    font-style: italic; font-size: 32px; line-height: 1;
  }
  .tagline {
    position: absolute; right: 24px; top: 60px; width: 220px;
    text-align: right;
    font-family: "Pinyon Script", cursive;
    font-size: 32px; line-height: 40px; color: var(--ink-soft);
  }
  .contact { position: absolute; left: 155px; top: 520px; }
  .contact__name { font-weight: 700; font-style: italic; font-size: 22px; line-height: 1; white-space: nowrap; }
  .contact__role { font-size: 17px; line-height: 1; margin-top: 2px; }
  .contact__address { font-size: 18px; line-height: 25px; margin-top: 22px; }
  .contact__list { list-style: none; margin-top: 18px; }
  .contact__item {
    display: flex; align-items: center; gap: 8px;
    font-size: 17px; line-height: 26px;
  }
  .contact__icon { width: 20px; height: 20px; flex: none; }
</style>
</head>
<body>
<main class="sheet">
  <section class="card card--front">
    <svg class="anatomy" role="img" aria-label="Anatomical illustration of the left half of a male muscular figure" viewBox="0 0 277 764" preserveAspectRatio="none">
      <defs>
        <linearGradient id="muscleFront" x1="0" y1="0" x2="1" y2="0">
          <stop offset="0" stop-color="var(--muscle-deep)" stop-opacity="0"/>
          <stop offset="0.35" stop-color="var(--muscle-mid)" stop-opacity="0.7"/>
          <stop offset="1" stop-color="var(--muscle-light)"/>
        </linearGradient>
      </defs>
      <rect width="277" height="764" fill="url(#muscleFront)"/>
    </svg>
    <div class="name-block">
      <div class="name-block__name">Garrick T Valbonne</div>
      <div class="name-block__title">LMT</div>
    </div>
  </section>

  <section class="card card--back">
    <svg class="anatomy" role="img" aria-label="Anatomical illustration of the right half of a male muscular figure" viewBox="0 0 290 764" preserveAspectRatio="none">
      <defs>
        <linearGradient id="muscleBack" x1="0" y1="0" x2="1" y2="0">
          <stop offset="0" stop-color="var(--muscle-light)"/>
          <stop offset="0.65" stop-color="var(--muscle-mid)" stop-opacity="0.7"/>
          <stop offset="1" stop-color="var(--muscle-deep)" stop-opacity="0"/>
        </linearGradient>
      </defs>
      <rect width="290" height="764" fill="url(#muscleBack)"/>
    </svg>
    <p class="tagline">Get a massage<br>for the health of it</p>
    <div class="contact">
      <div class="contact__name">GARRICK T VALBONNE</div>
      <div class="contact__role">Founder</div>
      <div class="contact__address">PO BOX 418 Harbour Lane<br>4th street Geelong</div>
      <ul class="contact__list">
        <li class="contact__item">
          <svg class="contact__icon" viewBox="0 0 20 20" fill="none" stroke="#fff" stroke-width="1.3"><circle cx="10" cy="10" r="9"/><rect x="7" y="5" width="6" height="10" rx="1"/></svg>
          (555) 014-2278
        </li>
        <li class="contact__item">
          <svg class="contact__icon" viewBox="0 0 20 20" fill="none" stroke="#fff" stroke-width="1.3"><circle cx="10" cy="10" r="9"/><rect x="5.5" y="6.5" width="9" height="7"/><path d="M5.5 6.5l4.5 4 4.5-4M5.5 13.5l3.3-3.3M14.5 13.5l-3.3-3.3"/></svg>
          hello@valbonnetouch.com
        </li>
        <li class="contact__item">
          <svg class="contact__icon" viewBox="0 0 20 20" fill="none" stroke="#fff" stroke-width="1.3"><circle cx="10" cy="10" r="9"/><circle cx="10" cy="10" r="5.5"/><ellipse cx="10" cy="10" rx="2.3" ry="5.5"/><path d="M4.5 10h11"/></svg>
          www.valbonnetouch.com
        </li>
      </ul>
    </div>
  </section>
</main>
</body>
</html>
```